Venue Booking Site

I would like a venue directory and booking website designed. The idea is that end users will come to the site to find venues for weddings, parties, events etc. They will be able to find the venue based on many criteria, the most important ones are availability and location - they will be able to see in real time which venues are available for the desired dates and areas.

Venues will be able to use the website as a reservation management tool, receive payments for bookings through the site and be able to manage bookings on the go. This will be made into an app. It needs to be developed in bootstrap. Brand name to be used: Mirqona. Venue, place and space bookings.

Target audience - end users - anyone who is looking for a venue. For Community members it will provide an easy way to find a suitable venue
Outline what dates and times the venue is available
Outline costs involved in booking the venue
Search via many other criteria
It will allow the customer to book and pay for the venue online in one smooth process

Clients: Venue managers - particularly focussing on not for profit businesses eg, GHAs, community hall managers, small business managers. These people typically use paper based systems yet and do not use websites so it needs to be very user friendly. Future growth to restaurants, pubs, event venues who have a stronger familiarity with computers and who might already use their own booking management tool - so this needs to be able to link in with their system.

What need will this meet for venue managers:
This tool provides venues with greater visibility, promotion and advertising of their venue
This allows more customers to find them and book with them
This tool will be offered to not-for-profit venue managers for free to better connect them to the community
This means greater profit for these community venues
This means more revenue and jobs created in these communities

Sample of the layout / contents attached. This is not a complete site map as yet as it is a work in progress for final pages.

Small Business

5+ page

Sans Serif

eb2027

• This is a psd file only - one template for each different section, home page, search page, detailed page view, admin back end
• does not need to be coded.
• Note, the golden lantern logo jpeg files were files we were toying with using for this project- but I am happy to use the main mirqona logo- I will let you decide.

```html
<!DOCTYPE html>
<html lang="en">
<head>
<meta charset="utf-8">
<title>Mirqona – Venue, place and space bookings</title>
<link href="https://fonts.googleapis.com/css2?family=Quicksand:wght@500;600&family=Open+Sans:wght@400;600&display=swap" rel="stylesheet">
<style>
:root{
  --blue:#1f6fce;
  --blue-dark:#1559b3;
  --orange:#f39322;
  --orange-dark:#ea8219;
  --orange-text:#f0901d;
  --text:#3a3a3a;
  --muted:#777;
  --line:#d6d6d6;
  --panel:#f3f3f3;
  --white:#fff;
}
*{box-sizing:border-box;margin:0;padding:0}
html,body{width:822px;height:1200px;overflow:hidden}
body{position:relative;background:var(--white);font-family:"Open Sans",sans-serif;color:var(--text)}
.abs{position:absolute}
.heading{font-family:"Quicksand",sans-serif;font-weight:500}

/* header */
.brand{left:100px;top:22px;font-family:"Quicksand",sans-serif;font-weight:600;font-size:29px;color:var(--blue);letter-spacing:-.3px}
.field{border:1px solid #cfcfcf;border-radius:12px;background:#fff;font-size:7.5px;color:#8a8a8a;padding:0 11px;display:flex;align-items:center;justify-content:space-between}
.top-search{left:350px;top:31px;width:187px;height:21px}
.btn{display:flex;align-items:center;justify-content:center;color:#fff;font-family:"Quicksand",sans-serif;font-weight:600}
.btn-login{left:548px;top:30px;width:83px;height:24px;background:var(--blue);font-size:10px}
.btn-list{left:637px;top:30px;width:83px;height:24px;background:var(--orange);font-size:10px}

/* nav */
.nav{left:0;top:74px;width:822px;height:33px;background:linear-gradient(#2a7ddc,#1a64c4);display:flex;align-items:center;padding-left:120px;gap:22px}
.nav a{color:#fff;text-decoration:none;font-family:"Quicksand",sans-serif;font-weight:600;font-size:11.5px}

/* hero */
.hero{left:0;top:107px;width:822px;height:305px;background:linear-gradient(100deg,#6f9a4c 0%,#c9d6c8 30%,#a9a49a 50%,#8a5a36 75%,#5a2e18 100%)}
.dots{left:382px;top:391px;display:flex;gap:4px}
.dots span{width:10px;height:10px;border-radius:50%;background:#fff}

/* search panel */
.finder{left:0;top:412px;width:822px;height:129px;background:linear-gradient(#f1f1f1,#f8f8f8);border-bottom:1px solid #e6e6e6}
.label{font-family:"Quicksand",sans-serif;font-weight:500;font-size:11.5px;color:#333}
.input{height:20px;border-radius:11px}
.btn-search{left:631px;top:499px;width:65px;height:21px;border-radius:11px;background:var(--orange);font-size:11px}

/* recent */
.recent-title{left:101px;top:564px;font-size:17.5px;color:#333}
.card{width:151px;height:179px;border:1px solid #e1e1e1;background:linear-gradient(#fff 60%,#f6f6f6)}
.card .photo{height:92px}
.card h3{position:absolute;left:12px;top:102px;font-family:"Quicksand",sans-serif;font-weight:600;font-size:10px;color:var(--orange-text)}
.card p{position:absolute;left:13px;font-size:7px;color:var(--muted)}
.card .desc{top:118px}
.card .city{top:133px}
.card .city b{font-weight:400;color:#333}
.card .more{position:absolute;left:10px;top:148px;width:60px;height:19px;border-radius:10px;background:linear-gradient(#2a7ddc,#1559b3);color:#fff;font-size:7.5px;font-weight:600;display:flex;align-items:center;justify-content:center}

/* footer */
.footer{left:0;top:1008px;width:822px;height:156px;background:linear-gradient(#f39a2c,#ee8a1e)}
.footer-col{top:1034px}
.footer-col h4{font-family:"Quicksand",sans-serif;font-weight:500;font-size:12.5px;color:#fff;margin-bottom:3px}
.footer-col li{list-style:none;font-size:8px;color:#fff;line-height:16px}
.divider{top:1038px;width:1px;height:84px;background:rgba(255,255,255,.35)}
.social{display:flex;gap:3px;margin-top:8px}
.social span{width:18px;height:18px;border-radius:50%;border:1.5px solid #fff}
.bottom-bar{left:0;top:1164px;width:822px;height:36px;background:var(--orange-dark)}
.copyright{left:118px;top:1178px;font-size:7px;color:rgba(255,255,255,.8)}
</style>
</head>
<body>

<header>
  <div class="abs brand">Mirqona</div>
  <div class="abs field top-search">Enter the number of people
    <svg width="10" height="10" viewBox="0 0 10 10"><circle cx="4" cy="4" r="3" fill="none" stroke="#999" stroke-width="1"/><line x1="6.3" y1="6.3" x2="9" y2="9" stroke="#999" stroke-width="1.2"/></svg>
  </div>
  <div class="abs btn btn-login">Login Venue</div>
  <div class="abs btn btn-list">List my venue</div>
</header>

<nav class="abs nav">
  <a href="#">Home</a><a href="#">About Us</a><a href="#">Venues</a><a href="#">News &amp; Offers</a><a href="#">Contact</a><a href="#">FAQs</a>
</nav>

<section class="abs hero" role="img" aria-label="Beachfront resort boardwalk with wicker lounge chairs, palm trees and a timber pavilion"></section>
<div class="abs dots"><span></span><span></span><span></span><span></span></div>

<section class="abs finder"></section>
<div class="abs label" style="left:104px;top:432px">Date of event:</div>
<div class="abs field input" style="left:104px;top:451px;width:80px">Date
  <svg width="8" height="5" viewBox="0 0 8 5"><path d="M1 1l3 3 3-3" fill="none" stroke="#666"/></svg></div>
<div class="abs field input" style="left:190px;top:451px;width:100px">Calendar selector
  <svg width="11" height="10" viewBox="0 0 11 10"><rect x=".5" y="1.5" width="10" height="8" fill="none" stroke="#888"/><line x1=".5" y1="3.5" x2="10.5" y2="3.5" stroke="#888"/><path d="M3 5.5h1M5 5.5h1M7 5.5h1M3 7.5h1M5 7.5h1M7 7.5h1" stroke="#888"/></svg></div>
<div class="abs label" style="left:305px;top:432px">Location:</div>
<div class="abs field input" style="left:305px;top:451px;width:187px">Enter a State, Suburb or postcode</div>
<div class="abs label" style="left:510px;top:432px">Venue Capacity:</div>
<div class="abs field input" style="left:508px;top:451px;width:188px">Enter the number of people</div>

<div class="abs label" style="left:104px;top:482px">Venue use:</div>
<div class="abs field input" style="left:103px;top:499px;width:187px">Select from the list
  <svg width="8" height="5" viewBox="0 0 8 5"><path d="M1 1l3 3 3-3" fill="none" stroke="#666"/></svg></div>
<div class="abs label" style="left:306px;top:482px">Keyword search:</div>
<div class="abs field input" style="left:305px;top:499px;width:187px">Type a keyword</div>
<div class="abs field input" style="left:508px;top:499px;width:115px">Advanced Search</div>
<div class="abs btn btn-search">Search</div>

<h2 class="abs heading recent-title">My Recent Searches</h2>

<article class="abs card" style="left:100px;top:597px"><div class="photo" role="img" aria-label="Hotel tower against blue sky" style="background:linear-gradient(90deg,#3a6fc0,#d8c7a6)"></div><h3>Venue Tittle Name</h3><p class="desc">Etiam est nunc venenatis in tris</p><p class="city">City Location: <b>New York</b></p><span class="more">Read More</span></article>
<article class="abs card" style="left:257px;top:597px"><div class="photo" role="img" aria-label="Seaside resort with white sails and pool" style="background:linear-gradient(#3f9fd8,#b9d7c7 60%,#6a8c4e)"></div><h3>Venue Tittle Name</h3><p class="desc">Etiam est nunc venenatis in tris</p><p class="city">City Location: <b>New York</b></p><span class="more">Read More</span></article>
<article class="abs card" style="left:414px;top:597px"><div class="photo" role="img" aria-label="Tropical beach with palms and turquoise sea" style="background:linear-gradient(#3b7bc8,#7fb6d6 60%,#e2dbc8)"></div><h3>Venue Tittle Name</h3><p class="desc">Etiam est nunc venenatis in tris</p><p class="city">City Location: <b>New York</b></p><span class="more">Read More</span></article>
<article class="abs card" style="left:571px;top:597px"><div class="photo" role="img" aria-label="Timber lodge building on a lawn" style="background:linear-gradient(#c9d6de,#7a5a3e 60%,#5d8a3a)"></div><h3>Venue Tittle Name</h3><p class="desc">Etiam est nunc venenatis in tris</p><p class="city">City Location: <b>New York</b></p><span class="more">Read More</span></article>

<article class="abs card" style="left:102px;top:789px"><div class="photo" role="img" aria-label="Brick hotel with blue entrance canopy" style="background:linear-gradient(#8a5a4a,#a05a3e 50%,#4f7a3c)"></div><h3>Venue Tittle Name</h3><p class="desc">Etiam est nunc venenatis in tris</p><p class="city">City Location: <b>New York</b></p><span class="more">Read More</span></article>
<article class="abs card" style="left:259px;top:789px"><div class="photo" role="img" aria-label="Terrace lounge at sunset" style="background:linear-gradient(#f0a24a,#8a5a3a 60%,#4a3424)"></div><h3>Venue Tittle Name</h3><p class="desc">Etiam est nunc venenatis in tris</p><p class="city">City Location: <b>New York</b></p><span class="more">Read More</span></article>
<article class="abs card" style="left:416px;top:789px"><div class="photo" role="img" aria-label="Resort infinity pool overlooking the sea" style="background:linear-gradient(#9ec2de,#d8c9a8 50%,#2a9ac8)"></div><h3>Venue Tittle Name</h3><p class="desc">Etiam est nunc venenatis in tris</p><p class="city">City Location: <b>New York</b></p><span class="more">Read More</span></article>
<article class="abs card" style="left:573px;top:789px"><div class="photo" role="img" aria-label="Large beachfront hotel with pool and umbrellas" style="background:linear-gradient(#6fa6d8,#d7ddd8 50%,#3f8a5a)"></div><h3>Venue Tittle Name</h3><p class="desc">Etiam est nunc venenatis in tris</p><p class="city">City Location: <b>New York</b></p><span class="more">Read More</span></article>

<footer>
  <div class="abs footer"></div>
  <div class="abs footer-col" style="left:112px"><h4>Company</h4><ul><li>About Us</li><li>Why Choose Us</li><li>Order Now</li><li>Special Offers</li></ul></div>
  <div class="abs divider" style="left:199px"></div>
  <div class="abs footer-col" style="left:234px"><h4>Services</h4><ul><li>Morbi porta</li><li>Libero ullamcorper</li><li>Nonummy nibh</li><li>Ligula pulvinar</li></ul></div>
  <div class="abs divider" style="left:326px"></div>
  <div class="abs footer-col" style="left:357px"><h4>Support</h4><ul><li>Metus eget</li><li>Consectetuer augue</li><li>Nisi quis</li><li>Lacus Utacmi</li></ul></div>
  <div class="abs divider" style="left:457px"></div>
  <div class="abs footer-col" style="left:486px"><h4>Resources</h4><ul><li>Testimonials</li><li>FAQ</li><li>Support</li><li>Term of Use</li></ul></div>
  <div class="abs divider" style="left:582px"></div>
  <div class="abs footer-col" style="left:614px"><h4>Follow Us</h4><ul><li style="font-size:7px">Get Connect with us on these</li></ul>
    <div class="social"><span></span><span></span><span></span><span></span></div></div>
  <div class="abs bottom-bar"></div>
  <div class="abs copyright">Copyright © 2014 Tavrel Foods | All Rights Reserved</div>
</footer>

</body>
</html>
```